Sign listing benefits of Wash and Fold Service

Sign 48 inches wide and 24 inches height to showcase service listed above.
Benefits include:
Saves Money
Saves Time
Convenient
Stain Treatment

Looking for something colorful (Blue and white are our business colors) the look of a laundromat business.

```html
<!DOCTYPE html>
<html lang="en">
<head>
<meta charset="utf-8">
<title>Wash and Fold Benefits Sign</title>
<link rel="stylesheet" href="https://fonts.googleapis.com/css2?family=Bebas+Neue&display=swap">
<style>
  :root {
    --page-bg: #e9e9e9;
    --sign-top: #02aaff;
    --sign-bottom: #038ffc;
    --white: #ffffff;
    --icon-line: #13a2f2;
    --foam: rgba(255, 255, 255, 0.95);
  }
  * { margin: 0; padding: 0; box-sizing: border-box; }
  html, body {
    width: 1200px;
    height: 1200px;
    overflow: hidden;
    background: var(--page-bg);
  }
  .sign {
    position: absolute;
    left: 40px;
    top: 320px;
    width: 1120px;
    height: 560px;
    background: linear-gradient(180deg, var(--sign-top) 0%, var(--sign-bottom) 100%);
    overflow: hidden;
  }
  .foam {
    position: absolute;
    border-radius: 50%;
  }
  .foam--top-right {
    right: -40px; top: -40px; width: 150px; height: 110px;
    background: radial-gradient(circle, var(--foam) 0%, rgba(255,255,255,0.6) 45%, rgba(255,255,255,0) 72%);
  }
  .foam--right {
    right: -70px; top: 130px; width: 140px; height: 260px;
    background: radial-gradient(ellipse, var(--foam) 0%, rgba(255,255,255,0.55) 45%, rgba(255,255,255,0) 72%);
  }
  .foam--bottom-right {
    right: -60px; bottom: -90px; width: 340px; height: 230px;
    background: radial-gradient(ellipse, var(--foam) 0%, rgba(255,255,255,0.7) 45%, rgba(255,255,255,0) 72%);
  }
  .foam--bottom-left {
    left: -60px; bottom: -70px; width: 260px; height: 170px;
    background: radial-gradient(ellipse, var(--foam) 0%, rgba(255,255,255,0.7) 45%, rgba(255,255,255,0) 72%);
  }
  .foam--left {
    left: -40px; top: 160px; width: 90px; height: 150px;
    background: radial-gradient(ellipse, rgba(255,255,255,0.45) 0%, rgba(255,255,255,0) 70%);
  }
  .benefit {
    position: absolute;
    display: flex;
    align-items: center;
  }
  .benefit__badge {
    width: 128px;
    height: 128px;
    flex: none;
  }
  .benefit__label {
    margin-left: 28px;
    font-family: 'Bebas Neue', 'Oswald', sans-serif;
    font-size: 71px;
    line-height: 0.93;
    color: var(--white);
    letter-spacing: 0.5px;
    white-space: nowrap;
  }
  .benefit--money { left: 108px; top: 125px; }
  .benefit--time { left: 605px; top: 125px; }
  .benefit--convenient { left: 108px; top: 300px; }
  .benefit--stain { left: 605px; top: 300px; }
  .benefit--stain .benefit__label { margin-top: -4px; }
</style>
</head>
<body>
  <main class="sign">
    <div class="foam foam--top-right" role="img" aria-label="Soap foam and bubbles"></div>
    <div class="foam foam--right" role="img" aria-label="Soap foam and bubbles"></div>
    <div class="foam foam--bottom-right" role="img" aria-label="Soap foam and bubbles"></div>
    <div class="foam foam--bottom-left" role="img" aria-label="Soap foam and bubbles"></div>
    <div class="foam foam--left" role="img" aria-label="Soap bubbles"></div>

    <section class="benefit benefit--money">
      <svg class="benefit__badge" viewBox="0 0 128 128" aria-hidden="true">
        <circle cx="64" cy="64" r="64" fill="#fff"/>
        <circle cx="64" cy="64" r="56" fill="none" stroke="var(--icon-line)" stroke-width="2.5"/>
        <g fill="none" stroke="var(--icon-line)" stroke-width="2.2" stroke-linecap="round" stroke-linejoin="round">
          <circle cx="64" cy="56" r="13"/>
          <path d="M68 50c-1-2-3-3-5-3-3 0-5 2-5 4 0 5 11 3 11 9 0 2-2 4-6 4-2 0-4-1-5-3M64 44v24"/>
          <path d="M64 32v6M58 34v3M70 34v3"/>
          <path d="M32 76h10v18H32zM42 80c6-3 12-3 18 0h10c3 0 3 5 0 5H58M42 91l14 2c6 0 24-8 32-14 2-1 4 1 2 3"/>
        </g>
      </svg>
      <h2 class="benefit__label">Saves Money</h2>
    </section>

    <section class="benefit benefit--time">
      <svg class="benefit__badge" viewBox="0 0 128 128" aria-hidden="true">
        <circle cx="64" cy="64" r="64" fill="#fff"/>
        <circle cx="64" cy="64" r="56" fill="none" stroke="var(--icon-line)" stroke-width="2.5"/>
        <g fill="none" stroke="var(--icon-line)" stroke-width="2.2" stroke-linecap="round" stroke-linejoin="round">
          <circle cx="64" cy="64" r="20"/>
          <path d="M64 96a32 32 0 1 1 28-47M92 38v11H81"/>
          <path d="M64 64l-7-7M64 64l9-5"/>
          <circle cx="64" cy="64" r="2"/>
          <path d="M64 47v3M64 78v3M47 64h3M78 64h3"/>
        </g>
      </svg>
      <h2 class="benefit__label">Saves Time</h2>
    </section>

    <section class="benefit benefit--convenient">
      <svg class="benefit__badge" viewBox="0 0 128 128" aria-hidden="true">
        <circle cx="64" cy="64" r="64" fill="#fff"/>
        <circle cx="64" cy="64" r="56" fill="none" stroke="var(--icon-line)" stroke-width="2.5"/>
        <g fill="none" stroke="var(--icon-line)" stroke-width="2.2" stroke-linecap="round" stroke-linejoin="round">
          <path d="M48 96V88c-6-5-9-12-9-20 0-6 3-10 8-10h10c4 0 6 3 5 6l-6 4M52 96h16v-6"/>
          <path d="M58 58l-4-14c-1-3 3-4 4-1l6 14"/>
          <circle cx="80" cy="74" r="14"/>
          <path d="M74 74l4 4 8-8"/>
        </g>
      </svg>
      <h2 class="benefit__label">Convenient</h2>
    </section>

    <section class="benefit benefit--stain">
      <svg class="benefit__badge" viewBox="0 0 128 128" aria-hidden="true">
        <circle cx="64" cy="64" r="64" fill="#fff"/>
        <circle cx="64" cy="64" r="56" fill="none" stroke="var(--icon-line)" stroke-width="2.5"/>
        <g fill="none" stroke="var(--icon-line)" stroke-width="2.2" stroke-linecap="round" stroke-linejoin="round">
          <path d="M54 36c3 4 17 4 20 0l16 8-4 14-8-3v40H50V55l-8 3-4-14z"/>
          <path d="M55 63c3-4 8-2 8 2s-5 3-3 7 6 5 2 8-9-2-9-6 0-7 2-11z"/>
          <path d="M72 56c2-1 4 1 3 3s-4 1-3-3zM74 78c2-1 4 1 3 3s-4 1-3-3z"/>
        </g>
      </svg>
      <h2 class="benefit__label">Stain<br>Treatment</h2>
    </section>
  </main>
</body>
</html>
```